Neuartiges Verpackungsdesign für Erdnüsse mit Karamell in Puzzleform
Zielgruppe
Wir gründen eine Produktion für Lebensmittel. Es handelt sich hierbei um Erdnüsse mit Karamell. Unsere Zielgruppe ist von jung bis alt, beider Geschlechter.
Aufgabenstellung
Bei dem Produkt handelt es sich um eine Weiterentwicklung eines Klassikers. Es werden Nüsse mit Karamell überzogen und zu verschiedenen Formen verarbeitet, die Besonderheit liegt darin das durch ein neues technisches Verfahren ein höher Nussanteil erreicht wird und das Produkt zudem optisch schöner und geschmacklich leichter und knuspriger wirkt als bei der Konkurrenz.
Zudem wird Erdnussöl sowie verschiedene hochwertige Zusatzstoffe hinzugegeben, somit erhält das Produkt mehr ungesättigte Fettsäuren und ist zudem nicht nur ein gesunder sondern auch ein besonders schmackhafter Snack. Außerdem ist noch zu erwähnen das, dass Produkt vegan ist und glutenfrei. Zudem soll es als proteinreich deklariert werden, da mehr Erdnüsse und weniger Zucker dosiert werden.
Die größte Besonderheit ist jedoch das, dass Produkt in jeglicher Form gebracht werden kann. Es sind somit nicht nur quadratische oder Riegelartige Formen möglich. Die Formen reichen von Kreisen, Dreiecken bis zu Weihnachtsmänner und Osterhasen, aufgrund der Vielzahl der Formen welche möglich sind wird das Produkt “Tobble Crunchies“ genannt. Die Hauptform welche angestrebt wird, ist eine Puzzleform. Also es ist ein Snack welcher eine Puzzle Form besitzt.
Die Verpackung soll einen Klotzbodenbeutel darstellen, also eine Verpackung welche beispielsweise den Tam Tel‘s ähnelt. Die Maße der Verpackung sind 85mm in Breite, 160mm in Höhe und 65mm in Tiefe.
Das ganze Design sollte sehr modern sein und edel wirken, wie es beispielsweise bei hochwertigen Schokoladen wie bei Morwe der Fall ist, da in unseren Produkt hochwertiges Erdnussöl zum Einsatz kommt.
Zudem soll das Design nicht nur die mittlere bis ältere Generation ansprechen, sondern auch die Jugend mit dem Ziel sich gesünder zu ernähren und es sollen sogar Kinder angesprochen werden, da sehr viele Formen möglich sind und Kinder damit Puzzlen oder spielen könnten, so ähnlich wie es bei Wippfrucht von Wb..

```html
<!DOCTYPE html>
<html lang="de">
<head>
<meta charset="utf-8">
<title>Erdnuss-Karamell-Bites – Verpackung</title>
<link rel="stylesheet" href="https://fonts.googleapis.com/css2?family=Fira+Sans:wght@400;500&family=Fira+Sans+Extra+Condensed:wght@500&family=Londrina+Solid:wght@400&display=swap">
<style>
  :root {
    --backdrop: #211e1a;
    --bag-orange: #c2681f;
    --bag-deep: #a9490f;
    --band-light: #dca676;
    --band-mid: #d08a4c;
    --ink: #2a140d;
    --paper: #f4f1ee;
    --label-grey: #dedbd9;
    --tagline-bg: #cfa07a;
    --peanut-gold: #d99a4e;
    --peanut-pale: #efc98f;
  }
  * { margin: 0; padding: 0; box-sizing: border-box; }
  html, body {
    width: 1091px; height: 1200px; overflow: hidden;
    background: var(--backdrop);
  }
  .canvas { position: relative; width: 1091px; height: 1200px; }
  .pack {
    position: absolute; left: 327px; top: 140px;
    width: 456px; height: 913px;
  }
  .pack-art { position: absolute; inset: 0; }
  .logo-slot {
    position: absolute; left: 117px; top: 111px;
    width: 207px; height: 60px;
    background: var(--label-grey);
    display: flex; align-items: center; justify-content: center;
    font-family: "Fira Sans", sans-serif; font-size: 17px; color: var(--ink);
    letter-spacing: 0.3px;
  }
  .tagline {
    position: absolute; left: 26px; top: 195px;
    width: 384px; height: 30px;
    background: var(--tagline-bg);
    display: flex; align-items: center; justify-content: center;
    font-family: "Fira Sans", sans-serif; font-weight: 500; font-size: 17px;
    color: var(--ink); letter-spacing: 0.2px; white-space: nowrap;
  }
  .product-name {
    position: absolute; left: 41px; top: 244px;
    font-family: "Londrina Solid", sans-serif; font-size: 66px; line-height: 70px;
    color: var(--ink); letter-spacing: 2px;
    text-shadow: 3px 3px 0 var(--paper);
  }
  .claims {
    position: absolute; left: 270px; top: 792px;
    list-style: none;
    font-family: "Fira Sans Extra Condensed", sans-serif; font-size: 25px; line-height: 30px;
    color: var(--paper);
  }
  .claims li { display: flex; align-items: center; gap: 9px; }
  .claims li::before {
    content: ""; width: 9px; height: 9px; border-radius: 50%;
    background: var(--ink); flex: none;
  }
</style>
</head>
<body>
<div class="canvas">
  <div class="pack">
    <svg class="pack-art" width="456" height="913" viewBox="0 0 456 913">
      <defs>
        <clipPath id="pack-outline"><rect x="0" y="0" width="456" height="913"/></clipPath>
        <linearGradient id="top-shade" x1="0" y1="0" x2="0" y2="1">
          <stop offset="0" stop-color="var(--bag-deep)"/>
          <stop offset="1" stop-color="var(--bag-orange)"/>
        </linearGradient>
        <radialGradient id="peanut-fill" cx="0.5" cy="0.5" r="0.5">
          <stop offset="0" stop-color="var(--peanut-pale)"/>
          <stop offset="0.7" stop-color="var(--peanut-gold)"/>
          <stop offset="1" stop-color="var(--peanut-gold)" stop-opacity="0"/>
        </radialGradient>
      </defs>
      <g clip-path="url(#pack-outline)">
        <rect class="pack-base" width="456" height="913" fill="url(#top-shade)"/>
        <path class="light-swoosh" fill="var(--band-mid)"
          d="M456 290 C360 340 250 400 150 500 C90 560 30 600 0 620 L0 760 C120 700 300 650 456 620 Z"/>
        <path class="light-swoosh" fill="var(--band-light)"
          d="M456 315 C360 360 260 420 170 520 C110 580 40 640 0 660 L0 880 C140 840 300 790 456 760 Z"/>
        <circle class="claim-disc" cx="690" cy="1005" r="130" fill="var(--bag-orange)"
          stroke="var(--ink)" stroke-width="4" transform="translate(-327 0)"/>
        <g role="img" aria-label="Foto: geröstete, geschälte Erdnüsse als Haufen">
          <ellipse cx="245" cy="570" rx="190" ry="255" fill="url(#peanut-fill)" opacity="0.85"/>
        </g>
      </g>
    </svg>

    <div class="logo-slot">LOGO PLATZHALTER</div>
    <div class="tagline">ERDNUSSWÜRFEL UMMANTELT IN KARAMELL</div>
    <h1 class="product-name">Erdnuss-<br>Karamell-<br>Bites</h1>
    <ul class="claims">
      <li>vegan</li>
      <li>proteinreich</li>
      <li>glutenfrei</li>
    </ul>
  </div>
</div>
</body>
</html>
```